Hydroponic Farm Needs a Business Card

We need a business card design for a hydroponic farm located on the Gulf Coast called 'Tallowbend Farms'. We grow many forms of lettuce and tomatoes along with other herbs and spices. We currently sell to farmer's markets though will soon be expanding to commercial accounts such as restaurants and grocery stores. The colors should be bright and vibrant to reflect the nature of our produce. The final design should communicate a professional, clean, yet friendly impression and able to be used both with farmer's markets and commercial accounts.

The pictures are an example of our product. The pictures do not have to be incorporated into the business card design.

Please put areas for information such as Names, Phone Number, E-mail address, and additional information.

Industry/Entity Type

Farm

```html
<!DOCTYPE html>
<html lang="en">
<head>
<meta charset="utf-8">
<title>Tallowbend Farms – Business Card</title>
<link rel="stylesheet" href="https://fonts.googleapis.com/css2?family=Courier+Prime&family=Kurale&display=swap">
<style>
  :root {
    --leaf-green: #acd431;
    --band-black: #1c1a1b;
    --tomato-red: #e8182a;
    --tomato-deep: #d9152a;
    --tomato-light: #f46a52;
    --highlight: #fff4f0;
    --text-white: #ffffff;
    --backdrop: #ece9e4;
    --card-shadow: rgba(0, 0, 0, 0.18);
  }
  * { box-sizing: border-box; margin: 0; padding: 0; }
  html, body {
    width: 1200px;
    height: 900px;
    overflow: hidden;
  }
  body {
    background: var(--backdrop);
    display: flex;
    flex-direction: column;
    align-items: center;
    justify-content: center;
    gap: 36px;
  }
  .card {
    position: relative;
    width: 700px;
    height: 400px;
    overflow: hidden;
    box-shadow: 0 6px 18px var(--card-shadow);
  }

  /* Back of card */
  .card-back { background: var(--leaf-green); }
  .card-back .web-band {
    position: absolute;
    left: 300px;
    right: 0;
    top: 120px;
    height: 44px;
    background: var(--band-black);
    display: flex;
    align-items: center;
    padding-left: 26px;
  }
  .card-back .web-address {
    font-family: "Kurale", serif;
    font-size: 16px;
    letter-spacing: 0.5px;
    color: var(--text-white);
  }

  /* Front of card */
  .card-front { display: flex; }
  .card-front .green-strip {
    width: 170px;
    background: var(--leaf-green);
  }
  .card-front .name-band {
    width: 88px;
    background: var(--band-black);
    position: relative;
    border-right: 3px solid var(--leaf-green);
  }
  .card-front .farm-name {
    position: absolute;
    left: 50%;
    top: 50%;
    transform: translate(-50%, -50%) rotate(-90deg);
    white-space: nowrap;
    font-family: "Courier Prime", monospace;
    font-size: 34px;
    letter-spacing: 1px;
    color: var(--text-white);
  }
  .card-front .info-panel {
    flex: 1;
    position: relative;
  }
  .card-front .produce-photo {
    position: absolute;
    inset: 0;
    background:
      radial-gradient(ellipse 190px 260px at 0% 12%, var(--highlight) 0%, rgba(255,244,240,0.5) 35%, rgba(255,244,240,0) 75%),
      radial-gradient(ellipse 200px 160px at 30% 90%, rgba(244,106,82,0.55) 0%, rgba(244,106,82,0) 80%),
      linear-gradient(160deg, var(--tomato-light) 0%, var(--tomato-red) 45%, var(--tomato-deep) 100%);
  }
  .card-front .identity {
    position: absolute;
    top: 92px;
    left: 60px;
    right: 40px;
    text-align: center;
    font-family: "Kurale", serif;
    color: var(--text-white);
  }
  .card-front .person-name { font-size: 34px; line-height: 1.15; }
  .card-front .person-role { font-size: 30px; line-height: 1.2; }
  .card-front .contact {
    position: absolute;
    left: 150px;
    bottom: 44px;
    font-family: "Kurale", serif;
    color: var(--text-white);
    line-height: 1.4;
  }
  .card-front .contact .tel,
  .card-front .contact .fax { font-size: 23px; }
  .card-front .contact .email { font-size: 19px; }
</style>
</head>
<body>
  <section class="card card-back">
    <div class="web-band">
      <span class="web-address">www. TallowbendFarm.com</span>
    </div>
  </section>

  <section class="card card-front">
    <div class="green-strip"></div>
    <div class="name-band">
      <span class="farm-name">Tallowbend Farms</span>
    </div>
    <div class="info-panel">
      <div class="produce-photo" role="img" aria-label="Close-up of a ripe red tomato with water droplets"></div>
      <div class="identity">
        <p class="person-name">Name&nbsp; Surname</p>
        <p class="person-role">Position</p>
      </div>
      <div class="contact">
        <p class="tel">Tel:&nbsp; 00 000 000 000</p>
        <p class="fax">Fax: 000 000 00</p>
        <p class="email">TallowbendFarm@greenmail.com</p>
      </div>
    </div>
  </section>
</body>
</html>
```